Brindle Works - Fast, Efficient and Gas Mainteance for Domestic, Commercial and Industrial clients

We are in the process of purchasing a new business and would like to get a new logo and business card.
Business is a gas maintenance business that also does new gas installations.
Has been established since 1988.
Services include:
Install all types of gas appliances & equipment inc. hot water units
Maintain / repair / replace all types of gas appliances & equipment

Target Market(s)

Domestic, Commercial and Industrial clients

Industry/Entity Type

Business

Contact Information for Business Card

admin@brindleworks-example.com.au
07 5981 4726
Brindle Works PTY LTD

Logo Text

Gas Fitting & Plumbing Maintenance Specialists

Font styles to use
Sans Serif

Requirements
Must have
• Logo
• Business name, contact number, email address, web address
• Domestic | Commercial | Industrial Est Since 1988
Nice to have
• Possibly a black card with a flame logo to one side
Should not have
• Spelling errors

```html
<!DOCTYPE html>
<html lang="en">
<head>
<meta charset="utf-8">
<title>Brindle Works Business Card</title>
<link rel="stylesheet" href="https://fonts.googleapis.com/css2?family=Arimo:wght@400;700&display=swap">
<style>
  :root {
    --page: #ffffff;
    --card: #000000;
    --brand-blue: #0a5bb5;
    --ink: #ffffff;
    --ink-soft: #cfd6df;
  }
  html, body {
    margin: 0;
    padding: 0;
    width: 1200px;
    height: 1200px;
    overflow: hidden;
    background: var(--page);
    font-family: "Arimo", Arial, sans-serif;
  }
  .canvas {
    position: relative;
    width: 1200px;
    height: 1200px;
  }
  .card {
    position: absolute;
    left: 224px;
    width: 804px;
    height: 446px;
    background: var(--card);
    border-radius: 32px;
    overflow: hidden;
  }
  .card--front { top: 130px; }
  .card--back { top: 636px; }

  .wordmark {
    position: absolute;
    margin: 0;
    font-weight: 700;
    color: var(--brand-blue);
    line-height: 1;
    letter-spacing: 1px;
    white-space: nowrap;
  }
  .card--front .wordmark {
    left: 0;
    right: 0;
    top: 176px;
    text-align: center;
    font-size: 92px;
  }
  .card--back .wordmark {
    left: 72px;
    top: 128px;
    font-size: 56px;
  }
  .company-name {
    position: absolute;
    left: 76px;
    top: 218px;
    margin: 0;
    font-size: 17px;
    line-height: 1;
    color: var(--ink);
    letter-spacing: 0.6px;
    white-space: nowrap;
  }
  .sectors {
    position: absolute;
    left: 76px;
    top: 244px;
    margin: 0;
    font-size: 12px;
    line-height: 1;
    color: var(--ink-soft);
    letter-spacing: 0.4px;
    white-space: nowrap;
  }
  .contact-list {
    position: absolute;
    left: 360px;
    top: 262px;
    margin: 0;
    padding: 0;
    list-style: none;
  }
  .contact-item {
    display: flex;
    align-items: center;
    height: 39px;
    font-size: 19px;
    color: var(--ink);
    letter-spacing: 0.3px;
    white-space: nowrap;
  }
  .contact-icon {
    width: 22px;
    height: 22px;
    margin-right: 13px;
    flex: none;
  }
</style>
</head>
<body>
<main class="canvas">
  <section class="card card--front">
    <p class="wordmark">BRINDLE</p>
  </section>

  <section class="card card--back">
    <p class="wordmark">BRINDLE</p>
    <p class="company-name">Brindle Works PTY LTD</p>
    <p class="sectors">Domestic | Commercial | Industrial &nbsp;Est Since 1988</p>
    <ul class="contact-list">
      <li class="contact-item">
        <svg class="contact-icon" viewBox="0 0 24 24" aria-hidden="true"><path d="M12 3 1 12h3v9h6v-6h4v6h6v-9h3z" fill="#fff"/></svg>
        Adress 01, Adress, City.
      </li>
      <li class="contact-item">
        <svg class="contact-icon" viewBox="0 0 24 24" aria-hidden="true"><path d="M6.6 2.5 9.5 7 7.6 9c1 2.7 3 5 5.6 6.4l2-1.8 4.4 3-1.8 3.4C11 19.5 4.5 12.5 3.5 5z" fill="#fff"/></svg>
        07 5981 4726
      </li>
      <li class="contact-item">
        <svg class="contact-icon" viewBox="0 0 24 24" aria-hidden="true"><circle cx="12" cy="12" r="4" fill="none" stroke="#fff" stroke-width="2.4"/><path d="M16 8v5.5a2.5 2.5 0 0 0 5 0V12a9 9 0 1 0-4 7.5" fill="none" stroke="#fff" stroke-width="2.4"/></svg>
        admin@brindleworks-example.com.au
      </li>
      <li class="contact-item">
        <svg class="contact-icon" viewBox="0 0 24 24" aria-hidden="true"><g fill="none" stroke="#fff" stroke-width="1.6"><circle cx="12" cy="12" r="10"/><ellipse cx="12" cy="12" rx="4.5" ry="10"/><path d="M2 12h20M3.5 7h17M3.5 17h17M12 2v20"/></g></svg>
        www.brindleworks-example.com.au
      </li>
    </ul>
  </section>
</main>
</body>
</html>
```